Brookmere Roofing Business Card

This is my current business card. But I’d like to make some changes. Somewhere on the card I’d like to list some of the services we offer. Maybe on the back? But I’d still like to keep the red. White and black modern look.

-residential & commercial roofing
-Roof Repairs & Maintenance
-Storm Damage & Insurance Claims specialist
-Christmas Lights and permanent Christmas lights
Fencing. Windows. Gutters. Siding. Sheetrock, painting.

```html
<!DOCTYPE html>
<html lang="en">
<head>
<meta charset="utf-8">
<title>Brookmere Roofing Business Card</title>
<link rel="stylesheet" href="https://fonts.googleapis.com/css2?family=Lato:wght@400;700;900&family=Michroma&display=swap">
<style>
  :root {
    --bg: #3a3a3a;
    --card: #050505;
    --red: #e0141b;
    --red-dark: #7a0c10;
    --white: #ffffff;
  }
  * { box-sizing: border-box; margin: 0; padding: 0; }
  html, body { width: 1200px; height: 694px; overflow: hidden; }
  body {
    background: var(--bg);
    font-family: "Lato", Arial, sans-serif;
    color: var(--white);
    display: flex;
    align-items: center;
    justify-content: center;
    gap: 24px;
  }
  .card {
    position: relative;
    width: 560px;
    height: 320px;
    background: var(--card);
    border-radius: 22px;
    overflow: hidden;
    box-shadow: 0 14px 30px rgba(0,0,0,0.45);
  }
  .card__band {
    position: absolute;
    left: 0; right: 0; bottom: 0;
    height: 16px;
    background: linear-gradient(90deg, var(--red-dark), var(--red) 50%, var(--red-dark));
  }
  .brand {
    display: flex;
    align-items: center;
    gap: 10px;
  }
  .brand__dot {
    width: 50px; height: 50px;
    border-radius: 50%;
    background: var(--red);
    flex: none;
  }
  .brand__name {
    font-weight: 900;
    font-size: 21px;
    line-height: 1.1;
    text-transform: uppercase;
    letter-spacing: 0.5px;
    color: var(--white);
    white-space: nowrap;
  }
  .divider {
    position: absolute;
    width: 2px;
    background: var(--red);
  }
  /* services side */
  .card--services .brand {
    position: absolute;
    left: 30px; top: 130px;
  }
  .card--services .divider {
    left: 258px; top: 44px;
    height: 222px;
  }
  .services {
    position: absolute;
    left: 284px; top: 52px;
    right: 18px;
    list-style: none;
    font-size: 15.5px;
    line-height: 1.4;
  }
  .services li {
    position: relative;
    padding-left: 16px;
    margin-bottom: 4px;
  }
  .services li::before {
    content: "";
    position: absolute;
    left: 0; top: 8px;
    width: 6px; height: 6px;
    border-radius: 50%;
    background: var(--red);
  }
  /* contact side */
  .card--contact .brand {
    position: absolute;
    left: 190px; top: 56px;
  }
  .person {
    position: absolute;
    left: 20px; top: 198px;
    width: 222px;
    text-align: right;
  }
  .person__name {
    font-family: "Michroma", Arial, sans-serif;
    font-size: 16px;
    color: var(--red);
    text-transform: uppercase;
    white-space: nowrap;
  }
  .person__name span { color: var(--white); }
  .person__role {
    font-size: 15px;
    margin-top: 6px;
  }
  .card--contact .divider {
    left: 262px; top: 180px;
    height: 86px;
  }
  .contacts {
    position: absolute;
    left: 282px; top: 184px;
    list-style: none;
    font-size: 15px;
  }
  .contacts li {
    display: flex;
    align-items: center;
    gap: 10px;
    margin-bottom: 9px;
  }
  .contacts svg { width: 16px; height: 16px; flex: none; }
</style>
</head>
<body>
  <section class="card card--services">
    <div class="brand">
      <div class="brand__dot"></div>
      <div class="brand__name">Brookmere<br>Roofing Co.</div>
    </div>
    <div class="divider"></div>
    <ul class="services">
      <li>Residential &amp; commercial roofing</li>
      <li>Roof Repairs &amp; Maintenance</li>
      <li>Storm Damage &amp; Insurance Claims specialist</li>
      <li>Christmas Lights and permanent Christmas lights</li>
      <li>Fencing. Windows. Gutters. Siding. Sheetrock, painting.</li>
    </ul>
    <div class="card__band"></div>
  </section>

  <section class="card card--contact">
    <div class="brand">
      <div class="brand__dot"></div>
      <div class="brand__name">Brookmere<br>Roofing Co.</div>
    </div>
    <div class="person">
      <div class="person__name">Dale <span>Morton</span></div>
      <div class="person__role">Owner</div>
    </div>
    <div class="divider"></div>
    <ul class="contacts">
      <li>
        <svg viewBox="0 0 16 16" aria-hidden="true"><path fill="#e0141b" d="M3 1.5l2.5-.5 1.5 3.5-1.6 1.2a8 8 0 0 0 4.9 4.9L11.5 9l3.5 1.5-.5 2.5c-.3 1.2-1.5 2-2.7 1.8C6.4 14 2 9.6 1.2 4.2 1 3 1.8 1.8 3 1.5z"/></svg>
        555-014-2290
      </li>
      <li>
        <svg viewBox="0 0 16 16" aria-hidden="true"><rect x="1" y="3" width="14" height="10" fill="#e0141b"/><path d="M1 3l7 6 7-6" fill="none" stroke="#050505" stroke-width="1.4"/></svg>
        dale@brookmereroofing.co
      </li>
      <li>
        <svg viewBox="0 0 16 16" aria-hidden="true"><circle cx="8" cy="8" r="7" fill="none" stroke="#e0141b" stroke-width="1.6"/><ellipse cx="8" cy="8" rx="3" ry="7" fill="none" stroke="#e0141b" stroke-width="1.2"/><path d="M1 8h14" stroke="#e0141b" stroke-width="1.2"/></svg>
        www.brookmereroofing.co
      </li>
    </ul>
    <div class="card__band"></div>
  </section>
</body>
</html>
```